Business Card & Logo Design Project

I am looking for a slick/simple design for a logo and business card, for a music Producer/Mixer/Engineer.

I'm based in Tokyo, Japan and I help my clients polish up their creation to major radio/TV status. My clients pay me for my taste, sense of balance expertise and creative direction/

Design should give impression of seal of quality, professionalism, and enthusiasm need some sort of a logo like design for "vantrix productions".

Please don't include music notes or instruments or anything musically related and anything samurai or ninja or too much Japan in them on the design.

I like clever, slick stuff that's not too obvious.
I also like a smooth gradation type transition. My favorite color is deep dark blue/

Good Luck and Thank you for your effort.
Updates

I would like a two-sided design for this one.
One side with "vantrix productions" (all lower case) on, and the other side with my name and contact info.

Please also consider portrait position (or direction).  (as opposed to landscape) 

Target Market(s)

My primary targets are artists & bands, who want absolute best for their creation.

Industry/Entity Type

Business

Requirements
Must have
• Two-Sided
1, vantrix productions
2, Kenji Harumoto, Producer/Mixer/Engineer, +81 090 4827 3516, brambleway@mailnest.example
Nice to have
• Any suggestions are welcome//
Should not have
• Anything music related images.
(e.g. CD, music notations, instruments etc.)

```html
<!DOCTYPE html>
<html lang="en">
<head>
<meta charset="utf-8">
<title>vantrix productions — business card</title>
<link rel="stylesheet" href="https://fonts.googleapis.com/css2?family=Mulish:wght@400;800&display=swap">
<style>
  :root {
    --page: #f1f1f1;
    --card-light: #29a8de;
    --card-dark: #1f86b9;
    --seal-light: #1a5a90;
    --seal-dark: #0d3f6e;
    --ink-deep: #1f3c4f;
    --ink-pale: #cce8f3;
    --ink-navy: #143d6b;
    --seal-text: #ffffff;
  }
  * { margin: 0; padding: 0; box-sizing: border-box; }
  html, body { width: 1200px; height: 1000px; overflow: hidden; background: var(--page); }
  .stage { position: relative; width: 1200px; height: 1000px; }
  .card {
    position: absolute; top: 72px; width: 490px; height: 854px;
    overflow: hidden; box-shadow: 0 2px 8px rgba(0,0,0,0.25);
    font-family: "Mulish", sans-serif;
  }
  .card--front { left: 55px; }
  .card--back { left: 655px; }
  .card svg { display: block; }
  .wordmark { font-weight: 400; letter-spacing: -2px; }
  .contact { font-weight: 800; fill: var(--ink-navy); }
</style>
</head>
<body>
<main class="stage">
  <section class="card card--front" aria-label="Front of card">
    <svg width="490" height="854" viewBox="0 0 490 854">
      <defs>
        <radialGradient id="cardGlow" cx="50%" cy="40%" r="70%">
          <stop offset="0" stop-color="var(--card-light)"/>
          <stop offset="1" stop-color="var(--card-dark)"/>
        </radialGradient>
        <radialGradient id="sealGlow" cx="50%" cy="40%" r="60%">
          <stop offset="0" stop-color="var(--seal-light)"/>
          <stop offset="1" stop-color="var(--seal-dark)"/>
        </radialGradient>
      </defs>
      <rect class="card-bg" width="490" height="854" fill="url(#cardGlow)"/>
      <circle class="seal" cx="245" cy="428" r="226" fill="url(#sealGlow)"/>
      <text class="seal-name" x="245" y="446" text-anchor="middle" font-size="52" font-weight="400" fill="var(--seal-text)">vantrix</text>
      <text class="wordmark" x="12" y="756" font-size="80" fill="var(--ink-deep)">vantrix</text>
      <text class="wordmark" x="52" y="818" font-size="80" fill="var(--ink-pale)">productions</text>
    </svg>
  </section>

  <section class="card card--back" aria-label="Back of card">
    <svg width="490" height="854" viewBox="0 0 490 854">
      <defs>
        <radialGradient id="cardGlowBack" cx="50%" cy="55%" r="70%">
          <stop offset="0" stop-color="var(--card-light)"/>
          <stop offset="1" stop-color="var(--card-dark)"/>
        </radialGradient>
        <radialGradient id="sealGlowBack" cx="50%" cy="40%" r="60%">
          <stop offset="0" stop-color="var(--seal-light)"/>
          <stop offset="1" stop-color="var(--seal-dark)"/>
        </radialGradient>
      </defs>
      <rect class="card-bg" width="490" height="854" fill="url(#cardGlowBack)"/>
      <text class="wordmark backdrop-word" transform="translate(40 -60) rotate(56)" font-size="170" fill="var(--ink-deep)">vantrix</text>
      <text class="wordmark backdrop-word" transform="translate(10 530) rotate(56)" font-size="170" fill="var(--ink-pale)">productions</text>
      <text class="contact contact-name" x="22" y="380" font-size="50">Kenji Harumoto</text>
      <text class="contact" x="22" y="424" font-size="31">Producer/Mixer/Engineer</text>
      <text class="contact" x="22" y="468" font-size="31">+81 090 4827 3516</text>
      <text class="contact" x="22" y="513" font-size="27">brambleway@mailnest.example</text>
      <circle class="seal" cx="92" cy="763" r="90" fill="url(#sealGlowBack)"/>
      <text class="seal-name" x="92" y="771" text-anchor="middle" font-size="24" font-weight="400" fill="var(--seal-text)">vantrix</text>
    </svg>
  </section>
</main>
</body>
</html>
```